Word template Letterhead for Australian Law Firm

We are a small law firm based in Manly, NSW, Australia. We have had a new logo designed for us and wish to freshen up the appearance of our letterhead. We require the letterhead to be in a word document that we can type over. This will not be a ‘printed’ letterhead because we send the majority of our correspondence via email. We would like to see a few options. We have attached our previous letterhead as well as the artwork for our new logo. We like the idea of a watermark across the bottom of the letter but the watermark must stay in place and we must be able to type over it. We are open to some colour throughout the letterhead because the majority of our correspondence is sent electronically. We also use electronic signatures. I have uploaded an example of this.The letterhead must include:-1. Our address details – including our phone number, physical address, website address etc. These details can be found on the copy of our previous letterhead;2. ABN Number;3. The words ‘Brevicor (NSW) Pty Ltd ACN 482 731 058 trading as Shipton & AssociatesLiability limited by a scheme approved under Professional Standards Legislation. The letterhead does not need to include the names and qualifications of the people working at the firm. Thank you.

Target Market(s)

Clients and other parties

Industry/Entity Type

Law Firm

Font styles to use
Other font styles liked:
• raleway, montserrat

Colors

Designer to choose colors to be used in the design.

Requirements
Must have
• Certain wording - please see project description.
• Must be a word document and must be able to type over the watermark etc.
Nice to have
• Watermark at the bottom of the letter.

```html
<!DOCTYPE html>
<html lang="en">
<head>
<meta charset="utf-8">
<title>Kervell &amp; Associates Letterhead</title>
<link href="https://fonts.googleapis.com/css2?family=Montserrat:ital,wght@0,400;0,600;0,700;1,400&display=swap" rel="stylesheet">
<style>
  :root {
    --backdrop: #d5dbed;
    --paper: #ffffff;
    --navy: #4b5aa6;
    --gold: #a8925e;
    --ink: #1e1e1e;
    --muted: #555;
    --badge: #1d1d1d;
    --badge-accent: #2f8fd0;
    --watermark-a: rgba(75, 90, 166, 0.09);
    --watermark-b: rgba(168, 146, 94, 0.07);
  }
  * { box-sizing: border-box; margin: 0; padding: 0; }
  html, body { width: 1200px; height: 900px; overflow: hidden; }
  body {
    background: var(--backdrop);
    font-family: "Montserrat", Arial, sans-serif;
    color: var(--ink);
  }
  .letterhead {
    position: absolute;
    left: 296px; top: 20px;
    width: 608px; height: 860px;
    background: var(--paper);
    box-shadow: 0 10px 30px rgba(60, 70, 110, 0.18);
  }
  .brand {
    position: absolute; top: 54px; left: 0; width: 100%;
    text-align: center;
  }
  .brand-mark {
    display: inline-block; width: 14px; height: 14px;
    border-radius: 50%; background: var(--navy);
    vertical-align: middle; margin-right: 6px;
  }
  .brand-name {
    font-weight: 700; font-size: 13px; letter-spacing: 1px;
    color: var(--navy); vertical-align: middle;
  }
  .brand-tag {
    display: block; margin-top: 4px;
    font-size: 6px; letter-spacing: 6px; color: var(--ink);
  }
  .header-rule { position: absolute; top: 96px; left: 0; width: 608px; height: 30px; }
  .specialist-badge {
    position: absolute; top: 126px; left: 36px;
    width: 30px; height: 30px; border-radius: 6px;
    background: var(--badge);
    border-left: 6px solid var(--badge-accent);
  }
  .contact {
    position: absolute; top: 128px; right: 40px;
    text-align: right; font-size: 10.5px; line-height: 15px;
  }
  .contact .address { color: var(--navy); text-transform: uppercase; margin-bottom: 8px; font-size: 10.5px; }
  .contact .label { color: var(--gold); text-transform: uppercase; }
  .contact .label.plain { text-transform: none; }
  .watermark {
    position: absolute; left: 40px; top: 300px;
    width: 520px; height: 240px; border-radius: 50%;
    background: radial-gradient(ellipse at 45% 40%, var(--watermark-a), var(--watermark-b) 55%, transparent 72%);
  }
  .body-copy {
    position: absolute; top: 256px; left: 40px; width: 528px;
    font-size: 10.5px; line-height: 13px;
  }
  .salutation { margin-bottom: 14px; }
  .paragraph { text-align: justify; }
  .sign-off {
    position: absolute; top: 620px; left: 40px;
    font-size: 11px;
  }
  .sign-off .closing { padding-left: 32px; }
  .sign-off .firm { font-weight: 700; font-size: 11.5px; margin-top: 2px; }
  .signature {
    width: 110px; height: 44px; margin: 12px 0 0 8px;
    background: linear-gradient(90deg, rgba(120,120,120,0.18), rgba(120,120,120,0.06));
    border-radius: 6px;
  }
  .legal-footer {
    position: absolute; top: 762px; left: 20px; width: 568px;
    text-align: center; font-style: italic; font-size: 9.5px; line-height: 13px;
  }
  .footer-rule {
    position: absolute; top: 812px; left: 184px; width: 240px;
    border-top: 1px solid var(--navy); opacity: 0.6;
  }
</style>
</head>
<body>
  <main class="letterhead">
    <header class="brand">
      <span class="brand-mark"></span><span class="brand-name">Kervell &amp; Associates</span>
      <span class="brand-tag">LAWYERS</span>
    </header>

    <svg class="header-rule" viewBox="0 0 608 30" aria-hidden="true">
      <path d="M30 4 Q300 30 578 14" fill="none" stroke="var(--navy)" stroke-width="1"/>
    </svg>

    <div class="specialist-badge" role="img" aria-label="Accreditation badge"></div>

    <address class="contact">
      <div class="address">Suite 4, 22 Corlett Lane<br>Fenwick NSW 2093</div>
      <div><span class="label">Telephone:</span> (02) 9000 4817</div>
      <div><span class="label">Facsimile:</span> (02) 9000 4818</div>
      <div><span class="label">Email:</span> reception@brevicorlaw.com.au</div>
      <div><span class="label">ABN:</span> 31 482 731 058</div>
      <div>www.kervellandassociates.com.au</div>
    </address>

    <div class="watermark" role="img" aria-label="Faint brand watermark"></div>

    <section class="body-copy">
      <p class="salutation">Dear Sir/Madam,</p>
      <p class="paragraph">Lorem ipsum, or lipsum as it is sometimes known, is dummy text used in laying out print, graphic or web designs. The passage is attributed to an unknown typesetter in the 15th century who is thought to have scrambled parts of Cicero's De Finibus Bonorum et Malorum for use in a type specimen book.</p>
    </section>

    <section class="sign-off">
      <p class="closing">Yours faithfully</p>
      <p class="firm">KERVELL &amp; ASSOCIATES</p>
      <div class="signature" role="img" aria-label="Electronic signature"></div>
    </section>

    <footer class="legal-footer">
      <p>Brevicor (NSW) Pty Ltd ACN 482 731 058 trading as Kervell &amp; Associates</p>
      <p>Liability limited by a scheme approved under Professional Standards Legislation. Legal practitioners at</p>
      <p>Brevicor (NSW) Pty Ltd are members of the scheme</p>
    </footer>
    <div class="footer-rule"></div>
  </main>
</body>
</html>
```